Flyer design for mailer

I want to take the attached information and make it look pretty in a similar fashion to our website > www.plumbrook.com for a mailer.
The final size should fit in a 6x9 envelope. Looking for a front and back. And QR code to our website.

```html
<!DOCTYPE html>
<html lang="en">
<head>
<meta charset="utf-8">
<title>Plumbrook Partners Mailer – Front and Back</title>
<link rel="stylesheet" href="https://fonts.googleapis.com/css2?family=Oswald:wght@600&family=PT+Sans+Narrow&family=Ubuntu:ital,wght@0,400;0,500;0,700;1,400;1,700&display=swap">
<style>
  :root {
    --maroon: #84171e;
    --olive: #85733a;
    --navy: #21367a;
    --white: #ffffff;
    --backdrop: #f3f1ec;
    --head: "Oswald", sans-serif;
    --body: "Ubuntu", sans-serif;
    --narrow: "PT Sans Narrow", sans-serif;
  }
  * { margin: 0; padding: 0; box-sizing: border-box; }
  html, body { width: 1200px; height: 1200px; overflow: hidden; }
  body { background: var(--backdrop); position: relative; font-family: var(--body); }

  .card { position: absolute; width: 480px; background: var(--white); overflow: hidden; }
  .card--front { left: 82px; top: 165px; height: 695px; }
  .card--back { left: 621px; top: 371px; height: 719px; }

  .abs { position: absolute; }

  /* front */
  .hello-art { left: 278px; top: 12px; width: 130px; height: 100px; border-radius: 14px;
    background: linear-gradient(135deg, #ef7d4f, #4fb2ac); }
  .foot-art { left: 22px; top: 47px; width: 150px; height: 416px; border-radius: 60px 60px 80px 80px;
    background: linear-gradient(180deg, var(--maroon), var(--olive)); opacity: .9; }

  .pitch { left: 193px; top: 147px; width: 285px; }
  .pitch__head { font-family: var(--head); font-weight: 600; color: var(--maroon);
    font-size: 29px; line-height: 43px; text-transform: uppercase; white-space: nowrap; letter-spacing: -.3px; }
  .pitch__lead { font-style: italic; color: var(--navy); font-size: 16px; line-height: 18.5px; margin-top: -4px; }
  .pitch__stat { font-weight: 700; color: var(--olive); font-size: 40px; line-height: 40px; margin-top: 4px; }
  .pitch__label { font-weight: 700; color: var(--olive); font-size: 18px; letter-spacing: 4.2px; line-height: 22px; }
  .pitch__big { font-weight: 500; color: var(--olive); font-size: 33px; line-height: 36px; }
  .pitch__big small { font-size: 19px; font-weight: 700; }
  .pitch__body { font-weight: 700; color: var(--navy); font-size: 18.5px; line-height: 25px; margin-top: 2px; }

  /* shared sign-off */
  .brand { display: flex; align-items: center; gap: 8px; }
  .brand__mark { width: 18px; height: 18px; background: var(--maroon); }
  .brand__name { font-family: var(--body); font-weight: 700; color: var(--maroon); font-size: 21px; line-height: 23px; text-transform: uppercase; }
  .divider { width: 1.5px; height: 66px; background: var(--olive); }
  .rep { white-space: nowrap; }
  .rep__name { font-weight: 700; font-style: italic; color: var(--maroon); font-size: 21px; line-height: 26px; }
  .rep__line { color: var(--olive); font-size: 12.5px; line-height: 16px; }
  .rep__web { color: var(--maroon); font-style: italic; font-size: 14px; line-height: 18px; }
  .foot-mini { width: 26px; height: 92px; border-radius: 13px;
    background: linear-gradient(180deg, var(--maroon), var(--olive)); }

  .band-thanks { left: 0; width: 480px; height: 27px; background: var(--olive); color: var(--white);
    font-weight: 700; font-size: 14px; line-height: 27px; text-align: center; }
  .band-contact { left: 0; width: 480px; background: var(--maroon); color: var(--white);
    font-size: 17.5px; line-height: 24px; padding: 4px 0 0 50px; border-top: 1px solid var(--white); }
  .band-contact strong { font-weight: 700; }

  /* back */
  .bubble { left: 0; top: 0; width: 480px; height: 300px; }
  .bubble__text { left: 202px; top: 52px; color: var(--white); font-weight: 700; font-style: italic;
    font-size: 50px; line-height: 68px; letter-spacing: .5px; }
  .tools { left: 24px; top: 200px; list-style: none; width: 452px; }
  .tools li { position: relative; padding-left: 16px; font-family: var(--narrow); color: var(--maroon);
    font-size: 20px; line-height: 24px; margin-bottom: 5px; white-space: nowrap; }
  .tools li::before { content: ""; position: absolute; left: 0; top: 7px; width: 10px; height: 10px;
    border-radius: 50%; background: var(--olive); }
  .tools li small { font-size: 12px; }
  .tools .tools__closing { font-size: 18.5px; letter-spacing: -.1px; }
</style>
</head>
<body>

<section class="card card--front">
  <div class="abs hello-art" role="img" aria-label="Hand-lettered 'Hello' in orange and teal"></div>
  <div class="abs foot-art" role="img" aria-label="Large footprint illustration with maroon toes and an olive arch"></div>

  <div class="abs pitch">
    <p class="pitch__head">Now that I’ve got<br>my foot in the door,</p>
    <p class="pitch__lead">I wanted to kick off a quick chat<br>about how we’ve helped</p>
    <p class="pitch__stat">1,200+ K-12</p>
    <p class="pitch__label">SCHOOL DISTRICTS</p>
    <p class="pitch__big">DIGITIZE 900 <small>million</small></p>
    <p class="pitch__body">records and move toward<br>paperless operations with<br>our cloud-based tools.</p>
  </div>

  <div class="abs brand" style="left:36px; top:518px;">
    <span class="brand__mark"></span>
    <span class="brand__name">Plumbrook<br>Partners</span>
  </div>
  <div class="abs divider" style="left:258px; top:506px;"></div>
  <div class="abs rep" style="left:278px; top:498px;">
    <p class="rep__name">Dana Whitfield</p>
    <p class="rep__line">Account Executive</p>
    <p class="rep__line">Plumbrook Partners</p>
    <p class="rep__web">www.plumbrook.com</p>
  </div>
  <div class="abs foot-mini" style="left:446px; top:482px;" role="img" aria-label="Small footprint illustration"></div>

  <p class="abs band-thanks" style="top:590px;">Thank you, and I can’t wait to take the next step with you!</p>
  <p class="abs band-contact" style="top:617px; height:78px;">Please reach out at DWhitfield@Plumbrook.com or<br><strong>give me a call on my cell at 555-014-2277.</strong></p>
</section>

<section class="card card--back">
  <svg class="abs bubble" viewBox="0 0 480 300" aria-hidden="true">
    <ellipse cx="302" cy="76" rx="180" ry="202" fill="var(--maroon)"/>
    <polygon points="140,140 110,188 168,168" fill="var(--maroon)"/>
  </svg>
  <p class="abs bubble__text">We have<br>tools for:</p>

  <ul class="abs tools">
    <li>Transcripts</li>
    <li>Hiring</li>
    <li>Onboarding/Offboarding</li>
    <li>Maintenance Requests</li>
    <li>Timesheets</li>
    <li>Substitute Management</li>
    <li>Professional Development Tracking</li>
    <li>Expense Reports <small>(integrated with RouteMap)</small></li>
    <li class="tools__closing">We can make any paper process completely electronic<br>with customized Workflows And we are developing more every year!</li>
  </ul>

  <div class="abs brand" style="left:36px; top:542px;">
    <span class="brand__mark"></span>
    <span class="brand__name">Plumbrook<br>Partners</span>
  </div>
  <div class="abs divider" style="left:253px; top:530px;"></div>
  <div class="abs rep" style="left:273px; top:522px;">
    <p class="rep__name">Dana Whitfield</p>
    <p class="rep__line">Account Executive</p>
    <p class="rep__line">Plumbrook Partners</p>
    <p class="rep__web">www.plumbrook.com</p>
  </div>
  <div class="abs foot-mini" style="left:446px; top:505px;" role="img" aria-label="Small footprint illustration"></div>

  <p class="abs band-thanks" style="top:613px;">Thank you, and I can’t wait to take the next step with you!</p>
  <p class="abs band-contact" style="top:640px; height:79px;">Please reach out at DWhitfield@Plumbrook.com or<br><strong>give me a call on my cell at 555-014-2277.</strong></p>
</section>

</body>
</html>
```